Advertising agency needs site design

You will be designing a clean (plenty of white space) and vivid (colorful) design that is for an advertising agency named Brightwell Reach. Their current web site is located at www.BrightwellReach.net. From there you can see their services and get a feel for the company as the site stands today.
The following are direct quotes from the client:
“I want a clean look with colors of the teal blue, deep yellow (in logo) and then a good energetic orange (deep orange - rich) should bring a good feel and enthusiasm.”
“The orange can be a nice accent color, not dominant.”
“Saw two other things I like - the website lanternkitestudio.com was pretty cool. I liked how the top banner changed colors as you moved to different tabs. I am somewhat wanting the colors I mentioned - like the blue color we use can be lighter as long as it works with the logo. - love the tulip forge site. I want quirky, creative and clean look - fun feel but slightly sophisticated to work with the medical field.”
Brightwell Reach currently focuses on the following primary industries:
• Medical / Health Care – Currently the primary industry
• Retail Industry
• Automotive Industry
• Entertainment Industry
Primary Services
• Media Planning & Buying: Web, TV, Print, Radio
• Campaign monitoring and reporting
• Commercial Production: TV & Radio
• Strategic Planning
• Market Research
• Internet Marketing: Email, SEO, Web design / development
Primary Navigation will consist of the following:
• Home
• About Us
o History
o Principal Profile (sub nav)
o Sales Team & Partners
• Clients
• Services
• Testimonials
• Contact Us
They want the web site to act as a basis for future marketing collateral so the overall feel from the web site must be capable of translating to print and other collateral. I do not currently have a clean digital version of their logo however their logo is on the web site (brightwellreach.net)
Reason: Still awaiting feedback from client on designs. They should be back to us shortly.
Target Market(s)
larger companies that are purchasing air time on television and radio. Typically in the health care industry and others described above in brief.
Industry/Entity Type
Advertising
Look and feel
Each slider illustrates characteristics of the customer's brand and the style your logo design should communicate.

```html
<!DOCTYPE html>
<html lang="en">
<head>
<meta charset="utf-8">
<title>Brightwell Reach — Advertising Agency</title>
<link href="https://fonts.googleapis.com/css2?family=Arimo:ital,wght@0,400;0,700;1,400&display=swap" rel="stylesheet">
<style>
:root{
  --page-bg:#e2ebf0;
  --ink-dark:#0b4f73;
  --teal:#16a9cf;
  --teal-deep:#0790b4;
  --teal-light:#3fc3e3;
  --heading-teal:#12a6cc;
  --orange:#ff8a12;
  --orange-deep:#f26f00;
  --body-grey:#4d4d4d;
  --white:#ffffff;
  --pale-cyan:#dff6fc;
}
*{box-sizing:border-box;margin:0;padding:0}
html,body{width:1200px;height:892px;overflow:hidden}
body{
  position:relative;
  font-family:"Arimo",Arial,sans-serif;
  background:linear-gradient(180deg,#cfe0e8 0,#eef5f8 120px,#ffffff 230px,#f4f8fa 380px,#dfe9ee 445px,var(--page-bg) 730px);
  color:var(--body-grey);
}
.abs{position:absolute}

/* header */
.brand{left:176px;top:43px;width:200px;white-space:nowrap;font-size:22px;font-weight:400;letter-spacing:1px;color:var(--ink-dark)}
.tagline{left:390px;top:54px;font-size:17px;color:#3eaad2;white-space:nowrap}
.phone{left:823px;top:50px;display:flex;align-items:center;gap:10px;font-size:30px;color:var(--ink-dark)}
.phone .lead{color:var(--teal)}

/* navigation */
.nav{left:141px;top:103px;width:918px;height:38px;border-radius:8px;
  background:linear-gradient(180deg,#5fd3ef 0,var(--teal) 45%,var(--teal-deep) 100%);
  box-shadow:0 0 0 1px #0d90b5 inset,0 8px 14px -6px rgba(0,80,110,.35)}
.nav ul{list-style:none;display:flex;position:absolute;left:38px;top:0;height:38px}
.nav li{height:38px;display:flex;align-items:center;padding:0 18px;font-size:13.5px;font-weight:700;color:var(--white);border-right:1px solid rgba(255,255,255,.25)}
.nav li:last-child{border:0}
.nav li.active{background:linear-gradient(180deg,#ffb14a,var(--orange) 60%,var(--orange-deep));height:45px;align-self:flex-start;padding:0 9px;margin-right:0}
.search{position:absolute;right:10px;top:8px;width:185px;height:22px;border-radius:11px;background:var(--white);overflow:hidden;display:flex}
.search span{flex:1;font-size:11.5px;color:#8a8a8a;padding:4px 0 0 14px}
.search b{width:32px;background:linear-gradient(180deg,#ffac3f,var(--orange-deep));display:flex;align-items:center;justify-content:center}

/* hero */
.hero-photo{left:178px;top:155px;width:422px;height:290px;border-radius:40px 40px 0 0;
  background:linear-gradient(180deg,rgba(160,205,225,.5),#8ec8e3 40%,#6fb4d6)}
.hero-title{left:640px;top:192px;font-size:52px;font-weight:700;color:var(--heading-teal);letter-spacing:-.5px;white-space:nowrap}
.hero-text{left:641px;top:262px;width:340px;font-size:13.5px;line-height:19px;color:var(--body-grey)}
.btn-more{left:818px;top:358px;width:136px;height:40px;border-radius:10px;
  background:linear-gradient(180deg,#ffd7a6 0,#ffa63b 45%,var(--orange-deep));
  box-shadow:0 0 0 1px #e07000 inset,0 8px 8px -4px rgba(0,0,0,.12);
  color:var(--white);font-size:21px;font-weight:700;text-align:center;line-height:40px}
.arrow{width:57px;height:57px;border-radius:50%;background:radial-gradient(circle at 40% 30%,#ffffff,#dfe5e8 70%,#c8d0d4);box-shadow:0 2px 4px rgba(0,0,0,.15);display:flex;align-items:center;justify-content:center}
.arrow.prev{left:142px;top:273px}
.arrow.next{left:1000px;top:273px}

/* info band */
.band{left:0;top:445px;width:1200px;height:284px;background:linear-gradient(180deg,var(--teal-light) 0,#12a8cd 45%,#0691b7 100%);box-shadow:0 1px 0 #7ad7ef inset}
.col-title{display:flex;align-items:center;gap:10px;height:40px;font-size:29px;font-weight:700;color:var(--white);text-shadow:0 1px 2px rgba(0,60,90,.45);white-space:nowrap}
.news{left:133px;top:464px;width:234px}
.news .col-title{padding-left:8px;margin-bottom:3px}
.news-item{padding:9px 8px 8px;border-bottom:1px solid rgba(255,255,255,.35);font-size:12px;line-height:17px;color:var(--pale-cyan)}
.news-item:last-child{border:0}
.news-item b{color:var(--white)}
.news-item i{color:var(--white)}
.divider{width:1px;top:480px;height:230px;background:linear-gradient(180deg,rgba(0,90,120,0),rgba(0,90,120,.35),rgba(0,90,120,0))}
.services{left:424px;top:464px;width:330px}
.services ul{list-style:none;margin-top:9px;font-size:11.5px;line-height:16.9px;color:var(--pale-cyan)}
.services li{padding-left:15px;white-space:nowrap}
.services li::before{content:"▪ ";font-size:9px}
.services li.group{padding-left:9px;font-weight:700;color:var(--white);font-size:12px}
.services li.group::before{content:""}
.testimonials{left:806px;top:464px;width:250px}
.quote-mark{left:786px;top:490px;font-size:100px;font-weight:700;color:rgba(255,255,255,.22);line-height:1}
.quote{margin:14px 0 0 5px;font-size:12px;line-height:17px;color:var(--pale-cyan)}
.cite{margin-top:16px;text-align:right;font-size:12px;line-height:17px;font-style:italic;color:var(--white)}

/* footer */
.footer{left:141px;top:729px;width:918px;height:106px;border-radius:0 0 20px 20px;background:linear-gradient(180deg,#e6eef2 0,#ffffff 45%)}
.foot-title{font-size:23px;color:var(--teal-light);font-weight:400;white-space:nowrap}
.newsletter{left:168px;top:743px}
.signup{margin-top:12px;display:flex;width:225px;height:24px;border-radius:12px;overflow:hidden;border:2px solid #d5dde1;background:var(--white)}
.signup span{flex:1;font-size:11.5px;color:#8d8d8d;padding:3px 0 0 13px}
.signup b{width:66px;background:linear-gradient(180deg,#ffa23a,var(--orange-deep));color:var(--white);font-size:12px;font-weight:400;text-align:center;line-height:20px}
.findus{left:512px;top:743px}
.social{display:flex;gap:7px;margin-top:9px}
.social span{width:30px;height:30px;border-radius:4px;display:block}
.social .s1{background:#5cc9ea}
.social .s2{background:#3b5a9b}
.social .s3{background:#c9302c}
.social .s4{background:#f0731c}
.contact{left:808px;top:743px}
.contact p{margin:8px 0 0 4px;font-size:12.5px;line-height:14px;color:#333}
.rights{left:0;width:1200px;top:850px;text-align:center;font-size:12.5px;color:#8a8f92}
</style>
</head>
<body>

<header>
  <div class="abs brand">Brightwell Reach</div>
  <div class="abs tagline">Sed ut perspiciatis unde omnis iste natus</div>
  <div class="abs phone">
    <svg width="36" height="26" viewBox="0 0 36 26" aria-hidden="true">
      <path d="M2 9c0-5 7-7 16-7s16 2 16 7v3h-8V8h-16v4H2z" fill="#6fc3de"/>
      <rect x="7" y="12" width="22" height="13" rx="3" fill="#6fc3de"/>
      <g fill="#fff"><circle cx="13" cy="16" r="1.4"/><circle cx="18" cy="16" r="1.4"/><circle cx="23" cy="16" r="1.4"/><circle cx="13" cy="20.5" r="1.4"/><circle cx="18" cy="20.5" r="1.4"/><circle cx="23" cy="20.5" r="1.4"/></g>
    </svg>
    <span><span class="lead">1000</span> 555.010</span>
  </div>

  <nav class="abs nav">
    <ul>
      <li class="active">Home</li>
      <li>About Us</li>
      <li>Clients</li>
      <li>Services</li>
      <li>Testimonials</li>
      <li>Contact Us</li>
    </ul>
    <div class="search"><span>Search</span><b>
      <svg width="14" height="14" viewBox="0 0 14 14" aria-hidden="true"><circle cx="5" cy="5" r="3.5" fill="none" stroke="#fff" stroke-width="1.8"/><path d="M8 8l5 5" stroke="#fff" stroke-width="2.2" stroke-linecap="round"/></svg>
    </b></div>
  </nav>
</header>

<section class="hero">
  <div class="abs hero-photo" role="img" aria-label="Photo of a medical team in light blue scrubs standing together"></div>
  <h1 class="abs hero-title">Medical care</h1>
  <p class="abs hero-text">Sed ut perspiciatis unde omnis iste natus error sit voluptatem accusantium doloremque laudantium, totam rem aperiam, eaque ipsa quae ab illo inventore veritatis et quasi architecto beatae vitae dicta sunt explicabo.</p>
  <div class="abs btn-more">read more</div>
  <div class="abs arrow prev"><svg width="26" height="28" viewBox="0 0 26 28" aria-hidden="true"><path d="M20 2L6 14l14 12" fill="none" stroke="#13a3cb" stroke-width="7" stroke-linejoin="round"/></svg></div>
  <div class="abs arrow next"><svg width="26" height="28" viewBox="0 0 26 28" aria-hidden="true"><path d="M6 2l14 12L6 26" fill="none" stroke="#13a3cb" stroke-width="7" stroke-linejoin="round"/></svg></div>
</section>

<section class="abs band"></section>

<div class="abs news">
  <h2 class="col-title">
    <svg width="44" height="34" viewBox="0 0 44 34" aria-hidden="true"><rect x="1" y="2" width="42" height="30" rx="2" fill="#f4f4f4" stroke="#bbb"/><rect x="5" y="6" width="34" height="5" fill="#777"/><g fill="#aaa"><rect x="5" y="14" width="15" height="2"/><rect x="5" y="18" width="15" height="2"/><rect x="5" y="22" width="15" height="2"/><rect x="5" y="26" width="15" height="2"/><rect x="24" y="14" width="15" height="14"/></g></svg>
    News
  </h2>
  <div class="news-item"><b>11.02.2011</b> - lorem ipsum dolor sit amet consectetur adipisicing... <i>read more</i></div>
  <div class="news-item"><b>11.02.2011</b> - lorem ipsum dolor sit amet consectetur adipisicing... <i>read more</i></div>
  <div class="news-item"><b>11.02.2011</b> - lorem ipsum dolor sit amet consectetur adipisicing... <i>read more</i></div>
  <div class="news-item"><b>11.02.2011</b> - lorem ipsum dolor sit amet consectetur adipisicing... <i>read more</i></div>
</div>

<div class="abs divider" style="left:396px"></div>

<div class="abs services">
  <h2 class="col-title">
    <svg width="40" height="38" viewBox="0 0 44 42" aria-hidden="true"><g fill="#e9eef1" stroke="#9aa6ad" stroke-width="1"><circle cx="16" cy="16" r="11"/><circle cx="32" cy="31" r="8"/></g><g fill="#9aa6ad"><circle cx="16" cy="16" r="4"/><circle cx="32" cy="31" r="3"/></g></svg>
    Services
  </h2>
  <ul>
    <li>Medical / Health Care</li>
    <li>Retail Industry</li>
    <li>Automotive Industry</li>
    <li>Entertainment Industry</li>
    <li class="group">Primary Services</li>
    <li>Media Planning &amp; Buying: Web, TV, Print, Radio</li>
    <li>Campaign monitoring and reporting</li>
    <li>Commercial Production: TV &amp; Radio</li>
    <li>Strategic Planning</li>
    <li>Market Research</li>
    <li>Internet Marketing: Email, SEO, Web design / development</li>
  </ul>
</div>

<div class="abs divider" style="left:770px"></div>

<div class="abs quote-mark">“</div>
<div class="abs testimonials">
  <h2 class="col-title">
    <svg width="44" height="36" viewBox="0 0 44 36" aria-hidden="true"><ellipse cx="17" cy="14" rx="15" ry="11" fill="#6ad0f2"/><ellipse cx="28" cy="22" rx="14" ry="10" fill="#8fd84a"/><path d="M30 30l6 6-1-8z" fill="#8fd84a"/></svg>
    Testimonials
  </h2>
  <p class="quote">"In the advertising world, I felt like a sheep among wolves. Brightwell Reach put me on a path that not only saved me money, but increased sales to my ideal target market. I would advise anyone to take advantage of Brightwell Reach's market knowledge, media connections and select demographic experience."</p>
  <p class="cite">R. Dunmore, Owner<br>Dunmore's Corner Lanes</p>
</div>

<footer>
  <div class="abs footer"></div>
  <div class="abs newsletter">
    <h3 class="foot-title">Newsletter</h3>
    <div class="signup"><span>e-mail address</span><b>subscribe</b></div>
  </div>
  <div class="abs findus">
    <h3 class="foot-title">Find us on</h3>
    <div class="social">
      <span class="s1" aria-label="Social link 1"></span>
      <span class="s2" aria-label="Social link 2"></span>
      <span class="s3" aria-label="Social link 3"></span>
      <span class="s4" aria-label="Feed link"></span>
    </div>
  </div>
  <div class="abs contact">
    <h3 class="foot-title">Contact details</h3>
    <p>Phone:<br>Address:<br>Email:</p>
  </div>
  <div class="abs rights">All rights reserved...</div>
</footer>

</body>
</html>
```